Business Card Design - Commercial Photographer

Professional Photographer requires eye catching creative business card. The design will need to incorporate my current logo in some form & not clash with my website tones & colours ( although website will be re designed in the future ). I'm currently shooting new folios in Commercial, Fashion & Architecture so I'm marketing to professional clients rather than portrait / wedding clients. Looking for something professional & creative.

Industry/Entity Type

Marketing

Requirements
Must have
• Website address - www.brightlenswork.com.au

Phone number - 0471586039

Email - info@brightlenswork.com.au

```html
<!DOCTYPE html>
<html lang="en">
<head>
<meta charset="utf-8">
<title>Bright Lens Work Photography – Business Card</title>
<link rel="stylesheet" href="https://fonts.googleapis.com/css2?family=Oswald:wght@400;500;600&display=swap">
<style>
  :root {
    --page-bg: #e9e6e2;
    --card-light-top: #f7f7f6;
    --card-light-bottom: #dcdcdb;
    --band-dark: #2b2b2c;
    --band-mid: #3d3d3e;
    --band-edge: #6f6f70;
    --logo-ink: #1f1f20;
    --logo-square: #b9b9bb;
    --name-ink: #f1e6e1;
    --contact-ink: #e6d8d2;
    --icon-ink: #d9c8c2;
  }
  * { margin: 0; padding: 0; box-sizing: border-box; }
  html, body {
    width: 1200px;
    height: 970px;
    overflow: hidden;
    background: var(--page-bg);
  }
  .canvas {
    position: relative;
    width: 1200px;
    height: 970px;
  }
  .business-card {
    position: absolute;
    left: 100px;
    top: 207px;
    width: 1000px;
    height: 556px;
    overflow: hidden;
    background: linear-gradient(180deg, var(--card-light-top) 0%, var(--card-light-bottom) 55%);
    box-shadow: 0 18px 40px rgba(0,0,0,0.18);
  }
  .card-wave {
    position: absolute;
    inset: 0;
    width: 1000px;
    height: 556px;
  }
  .brand {
    position: absolute;
    left: 305px;
    top: 100px;
    display: flex;
    align-items: center;
    gap: 18px;
  }
  .brand-square {
    width: 58px;
    height: 58px;
    background: var(--logo-square);
  }
  .brand-words {
    display: flex;
    flex-direction: column;
    align-items: flex-end;
    font-family: "Oswald", sans-serif;
    font-weight: 600;
    color: var(--logo-ink);
    text-transform: uppercase;
    line-height: 1;
  }
  .brand-name {
    font-size: 36px;
    letter-spacing: 0.5px;
  }
  .brand-tagline {
    font-size: 16px;
    letter-spacing: 2px;
    margin-top: 4px;
  }
  .holder-name {
    position: absolute;
    left: 209px;
    top: 380px;
    font-family: "Oswald", sans-serif;
    font-weight: 500;
    font-size: 34px;
    letter-spacing: 1px;
    color: var(--name-ink);
    text-transform: uppercase;
  }
  .contact-list {
    position: absolute;
    left: 466px;
    top: 376px;
    list-style: none;
  }
  .contact-item {
    display: flex;
    align-items: center;
    height: 50px;
    font-family: "Oswald", sans-serif;
    font-weight: 400;
    font-size: 25px;
    color: var(--contact-ink);
    letter-spacing: 0.3px;
  }
  .contact-icon {
    width: 28px;
    height: 28px;
    margin-right: 40px;
    flex: none;
  }
</style>
</head>
<body>
<main class="canvas">
  <section class="business-card" aria-label="Business card for Bright Lens Work Photography">
    <svg class="card-wave" viewBox="0 0 1000 556" aria-hidden="true">
      <defs>
        <linearGradient id="bandFill" x1="0" y1="0" x2="0" y2="1">
          <stop offset="0" stop-color="var(--band-mid)"/>
          <stop offset="1" stop-color="var(--band-dark)"/>
        </linearGradient>
      </defs>
      <path d="M0 196 C 90 300, 190 318, 320 292 C 470 262, 560 206, 700 196 C 820 188, 920 220, 1000 262 L1000 556 L0 556 Z"
            fill="var(--band-edge)"/>
      <path d="M0 210 C 90 312, 190 330, 320 304 C 470 274, 560 218, 700 208 C 820 200, 920 232, 1000 274 L1000 556 L0 556 Z"
            fill="url(#bandFill)"/>
      <path d="M760 205 L1000 380 L1000 274 Z" fill="#ffffff" fill-opacity="0.05"/>
      <path d="M640 230 L900 556 L1000 556 L1000 420 Z" fill="#000000" fill-opacity="0.08"/>
    </svg>

    <div class="brand">
      <div class="brand-square"></div>
      <div class="brand-words">
        <span class="brand-name">Bright Lens Work</span>
        <span class="brand-tagline">Photography</span>
      </div>
    </div>

    <h1 class="holder-name">Mara Ellison</h1>

    <ul class="contact-list">
      <li class="contact-item">
        <svg class="contact-icon" viewBox="0 0 28 28" aria-hidden="true">
          <path d="M4 11 C4 6, 24 6, 24 11 L20 12 L19 9 L9 9 L8 12 Z" fill="none" stroke="var(--icon-ink)" stroke-width="2" stroke-linejoin="round"/>
          <rect x="7" y="14" width="14" height="9" rx="2" fill="none" stroke="var(--icon-ink)" stroke-width="2"/>
          <circle cx="14" cy="18.5" r="2" fill="var(--icon-ink)"/>
        </svg>
        <span>0471586039</span>
      </li>
      <li class="contact-item">
        <svg class="contact-icon" viewBox="0 0 28 28" aria-hidden="true">
          <rect x="4" y="7" width="20" height="14" fill="none" stroke="var(--icon-ink)" stroke-width="2"/>
          <path d="M4 7 L14 15 L24 7" fill="none" stroke="var(--icon-ink)" stroke-width="2"/>
        </svg>
        <span>info@brightlenswork.com.au</span>
      </li>
      <li class="contact-item">
        <svg class="contact-icon" viewBox="0 0 28 28" aria-hidden="true">
          <circle cx="14" cy="14" r="10" fill="none" stroke="var(--icon-ink)" stroke-width="2"/>
          <ellipse cx="14" cy="14" rx="4.5" ry="10" fill="none" stroke="var(--icon-ink)" stroke-width="1.6"/>
          <line x1="4" y1="14" x2="24" y2="14" stroke="var(--icon-ink)" stroke-width="1.6"/>
        </svg>
        <span>www.brightlenswork.com.au</span>
      </li>
    </ul>
  </section>
</main>
</body>
</html>
```